Silver Harbor Dental

I need a business card design for a state of the art and very modern dental practice. We provide general and pediatric dental services. I have attached a black and white EPS file of our logo, s logo design is not required. I have also attached two colors for our background and font. It does not have to be these two colors only. I am open to any suggestions. I have also included our current business card.
Things that should be different from our current business card is the logo, the website now is "www.silverhdental.com".
On the top right, where it says "like us on friendloop", now should say "Download our app on tap bazaar and vexa shelf store", but instead of our app, it should show the icon of our app, instead of tap bazaar and vexa shelf, it should show their icons, and not spell the words out.
I have also attached what the front of the card should more or less look like. It is the one with the different size fonts. I need the icon for phone, email, address, etc next to each. It is the file name "back of the businesscard1".

Target Market(s)

18-35 year-olds

Industry/Entity Type

Dental

Requirements
Nice to have
• the icon of our app, ormlist, and vexa shelf on the top right.

```html
<!DOCTYPE html>
<html lang="en">
<head>
<meta charset="utf-8">
<title>Silver Harbor Dental — Business Card</title>
<link rel="stylesheet" href="https://fonts.googleapis.com/css2?family=Source+Sans+3:ital,wght@0,400;0,600;0,700;1,600&display=swap">
<style>
  :root {
    --sky: #9dd9ec;
    --sky-soft: #b4e3f1;
    --navy: #136a9f;
    --ink: #1b6aa0;
    --white: #ffffff;
    --rule: #bfe3ef;
    --frame: #d8d8d8;
    --page: #ffffff;
  }
  * { box-sizing: border-box; margin: 0; padding: 0; }
  html, body { width: 1200px; height: 848px; overflow: hidden; background: var(--page); }
  body { position: relative; font-family: "Source Sans 3", sans-serif; }
  .sheet { position: absolute; inset: 0; border: 1px solid var(--frame); }

  .card { position: absolute; left: 343px; width: 479px; }

  /* Front */
  .card-front { top: 121px; height: 293px; background: var(--sky); overflow: hidden; }
  .brand { position: absolute; left: 24px; top: 90px; color: var(--ink); }
  .brand-name { font-size: 26px; font-weight: 400; letter-spacing: 0.5px; line-height: 1; }
  .brand-tagline { margin-top: 6px; font-size: 13px; font-weight: 600; font-style: italic; }
  .mirror-art { position: absolute; left: 299px; top: 0; width: 132px; height: 118px;
    background: linear-gradient(160deg, var(--sky-soft), var(--sky)); border-radius: 0 0 60px 20px; }

  .download { position: absolute; right: 18px; top: 11px; text-align: center; color: var(--ink); }
  .download-title { font-size: 9px; font-weight: 600; letter-spacing: 0.4px; }
  .store-list { display: flex; gap: 8px; margin-top: 5px; list-style: none; }
  .store { display: flex; flex-direction: column; align-items: center; gap: 2px; font-size: 8px; font-weight: 600; }
  .store-dot { width: 24px; height: 24px; border-radius: 50%; background: var(--navy); border: 2px solid var(--white); }

  .person { position: absolute; left: 27px; top: 189px; color: var(--white); font-size: 19px; font-weight: 600; }
  .person-title { font-size: 13px; font-weight: 400; color: var(--sky-soft); filter: brightness(1.15); }
  .contact { position: absolute; left: 201px; top: 190px; color: var(--ink); font-size: 14px; line-height: 21.5px; list-style: none; }
  .contact b { font-weight: 600; }
  .web-band { position: absolute; left: 0; bottom: 0; width: 100%; height: 34px; background: var(--navy);
    color: var(--white); font-size: 16px; font-weight: 600; padding: 5px 0 0 201px; }

  /* Back */
  .card-back { top: 449px; height: 292px; background: var(--white); border: 1px solid var(--frame); }
  .appt { position: absolute; left: 33px; top: 53px; width: 413px; color: var(--ink); }
  .appt-title { color: var(--sky); font-size: 19px; font-weight: 700; letter-spacing: 1px; }
  .appt-field { height: 36px; padding-top: 12px; border-bottom: 1px solid var(--rule); font-size: 18px; font-weight: 600; }
  .appt-field:first-of-type { height: 30px; padding-top: 6px; }
  .appt-note { margin-top: 13px; font-size: 13.5px; line-height: 20px; }
  .phone-band { position: absolute; left: 0; bottom: 0; width: 100%; height: 32px; background: var(--sky);
    color: var(--white); font-size: 17px; font-weight: 600; padding: 4px 0 0 33px; }
</style>
</head>
<body>
<div class="sheet">

  <section class="card card-front">
    <div class="mirror-art" role="img" aria-label="Dental mirror illustration"></div>

    <div class="brand">
      <p class="brand-name">Silver Harbor Dental</p>
      <p class="brand-tagline">General and Pediatric Dentistry</p>
    </div>

    <div class="download">
      <p class="download-title">DOWNLOAD</p>
      <ul class="store-list">
        <li class="store"><span class="store-dot"></span>Silver Harbor</li>
        <li class="store"><span class="store-dot"></span>ormlist</li>
        <li class="store"><span class="store-dot"></span>vexa shelf</li>
      </ul>
    </div>

    <p class="person">Daniel Reyes <span class="person-title">DDS</span></p>
    <ul class="contact">
      <li>482 Marlowe Avenue, Brookfield, NY, 11250</li>
      <li><b>T:</b> (718)555-0142 &nbsp;<b>C:</b> (917)555-0193</li>
      <li><b>E:</b> silverharbordentalpc@mail.com</li>
    </ul>
    <div class="web-band">www.silverhdental.com</div>
  </section>

  <section class="card card-back">
    <div class="appt">
      <h2 class="appt-title">APPOINTMENT</h2>
      <p class="appt-field">Name:</p>
      <p class="appt-field">Date:</p>
      <p class="appt-field">Time:</p>
      <p class="appt-note">If you are unable to keep your appointment,<br>please notify us as soon as possible.</p>
    </div>
    <div class="phone-band">T: (718)555-0142 &nbsp;C: (917)555-0193</div>
  </section>

</div>
</body>
</html>
```